Modern web-site for a game changer new health app!

We need a very clean UX / UI design for our company website that will be used to sell our brand to large corporations and their employees. If we find a good match, we'd need you to do the app design and some graphics for ongoing design needs.

For a first of its kind app developed at Whitcombe University, making licensed holistic medicine accessible to everyday people through access and curation by democratizing holistic health.

Please read the details attached thoroughly and reach out if you have any questions. Many thanks!
Updates

I've updated our requirements to make it easier, please review new details in the PDF shared. Many thanks!

Final brief refinement just uploaded, much has been simplified with very clear guidelines, please update and apply. thanks much!

Target Market(s)

corporate employees and large C level corporate leaders

Industry/Entity Type

wellness

Number of Pages Required

4 page

Font styles to use
Other font styles liked:
• We need website design now and app and socials after, hoping the designer we choose now can work with us on a regular basis going forward

Requirements
Must have
• clean, modern, minimal rich
Nice to have
• some added touches to give a custom feel
Should not have
• pictures, natural looking images or shapes

```html
<!DOCTYPE html>
<html lang="en">
<head>
<meta charset="utf-8">
<title>Verdi — Health for everyone</title>
<link href="https://fonts.googleapis.com/css2?family=Inter:wght@400;500;600;700;800&display=swap" rel="stylesheet">
<style>
  :root {
    --orange: #ff8a00;
    --yellow: #ffd600;
    --ink: #111111;
    --black: #000000;
    --white: #ffffff;
    --paper: #efefef;
    --card: #f6f6f6;
    --line: #dddddd;
    --muted: #c4c4c4;
    --grad: linear-gradient(90deg, var(--orange), var(--yellow));
  }
  * { box-sizing: border-box; margin: 0; padding: 0; }
  html, body { width: 1200px; height: 4580px; overflow: hidden; }
  body { font-family: "Inter", Arial, sans-serif; color: var(--ink); background: var(--white); position: relative; }
  section, header, footer { position: absolute; left: 0; width: 1200px; }
  .abs { position: absolute; }
  .accent { color: var(--orange); }
  .accent-y { color: var(--yellow); }
  .btn { position: absolute; display: flex; align-items: center; justify-content: center; background: var(--grad); color: var(--white); font-size: 13px; font-weight: 500; }
  .wordmark { font-weight: 800; font-size: 40px; color: var(--orange); letter-spacing: 1px; }

  /* header */
  .site-header { top: 0; height: 135px; background: var(--white); }
  .site-header .wordmark { left: 62px; top: 48px; }
  .nav { position: absolute; right: 62px; top: 60px; display: flex; gap: 34px; align-items: center; font-size: 15px; font-weight: 500; }
  .nav .contact { background: var(--grad); color: var(--white); padding: 6px 14px; }

  /* hero */
  .hero { top: 135px; height: 450px; background: var(--black); overflow: hidden; }
  .hero-art { position: absolute; inset: 0; background: radial-gradient(ellipse 300px 240px at 870px 210px, #f4e8ea 0%, #d9b7c0 35%, #3c4a2c 65%, transparent 80%), linear-gradient(90deg, #1f3a1d 0%, #0b120a 35%, #050505 100%); }
  .hero h1 { position: absolute; left: 60px; top: 60px; color: var(--white); font-size: 92px; line-height: 114px; font-weight: 800; }
  .hero p { position: absolute; left: 62px; top: 323px; width: 420px; color: var(--white); font-size: 13px; line-height: 18px; }
  .play { position: absolute; left: 850px; top: 200px; width: 52px; height: 52px; border-radius: 50%; background: var(--white); display: flex; align-items: center; justify-content: center; }

  /* features */
  .features { top: 585px; height: 410px; background: var(--paper); }
  .feature { position: absolute; width: 348px; height: 134px; background: var(--white); border: 1px solid var(--line); display: flex; align-items: center; gap: 28px; padding-left: 30px; font-size: 17px; font-weight: 600; line-height: 22px; }
  .feature svg { flex: none; }

  /* how it works */
  .how { top: 995px; height: 450px; background: var(--white); }
  .how h2 { position: absolute; left: 60px; top: 70px; font-size: 54px; font-weight: 800; }
  .how .copy { position: absolute; left: 62px; top: 160px; width: 420px; font-size: 13px; line-height: 22px; }
  .how .copy p + p { margin-top: 10px; }
  .step-num { position: absolute; left: 695px; font-size: 66px; font-weight: 800; color: var(--muted); }
  .step { position: absolute; left: 804px; width: 334px; height: 88px; background: var(--card); border: 1px solid var(--line); display: flex; align-items: center; gap: 22px; padding-left: 26px; font-size: 18px; font-weight: 600; line-height: 22px; }

  /* pattern bands */
  .pattern { height: 90px; }
  .pattern-dark { top: 1445px; background: linear-gradient(180deg, #2a2a2a, #111111); }
  .pattern-light { top: 3054px; height: 93px; background: linear-gradient(180deg, #d9d9d9, #c9c9c9); }

  /* trust */
  .trust { top: 1533px; height: 584px; background: var(--black); color: var(--white); }
  .trust h2 { position: absolute; left: 60px; top: 82px; width: 1100px; font-size: 56px; line-height: 69px; font-weight: 700; }
  .pillar { position: absolute; top: 286px; width: 348px; height: 216px; background: var(--white); color: var(--ink); display: flex; flex-direction: column; align-items: center; justify-content: center; gap: 28px; font-size: 22px; font-weight: 600; }
  .trusted { position: absolute; left: 0; width: 1200px; top: 532px; text-align: center; font-size: 21px; font-weight: 600; }

  /* enterprise */
  .enterprise { top: 2117px; height: 554px; background: var(--white); }
  .enterprise h2 { position: absolute; left: 62px; top: 62px; font-size: 56px; line-height: 68px; font-weight: 700; }
  .enterprise .lead { position: absolute; left: 62px; top: 222px; width: 320px; font-size: 19px; line-height: 30px; }
  .enterprise .body { position: absolute; left: 62px; top: 290px; width: 420px; font-size: 13px; line-height: 22px; }
  .enterprise .body p + p { margin-top: 14px; }
  .spa-art { position: absolute; left: 590px; top: 100px; width: 535px; height: 375px; border-radius: 48%; background: radial-gradient(circle at 50% 45%, #e8b878 0%, #c98d55 30%, #e4d9d3 55%, rgba(255,255,255,0) 75%); }

  /* human care */
  .care { top: 2671px; height: 383px; background: var(--paper); }
  .care h2 { position: absolute; left: 60px; top: 56px; font-size: 56px; line-height: 69px; font-weight: 700; }
  .care .copy { position: absolute; left: 62px; top: 206px; font-size: 13px; line-height: 30px; }
  .rings { position: absolute; left: 883px; top: 57px; width: 253px; height: 253px; border-radius: 50%; background: radial-gradient(circle, var(--yellow) 0%, #ffe979 40%, var(--orange) 100%); opacity: .85; }

  /* stats */
  .stats { top: 3147px; height: 804px; background: var(--white); }
  .stat-box { position: absolute; background: var(--paper); }
  .stat-left { left: 62px; top: 78px; width: 665px; height: 282px; }
  .stat-right { left: 752px; top: 78px; width: 384px; height: 282px; }
  .stat-left .claim { position: absolute; left: 30px; top: 85px; width: 240px; font-size: 26px; line-height: 32px; font-weight: 700; }
  .big { position: absolute; font-size: 70px; font-weight: 800; }
  .stat-right h3 { position: absolute; left: 30px; top: 32px; width: 330px; font-size: 26px; line-height: 32px; font-weight: 700; }
  .quote { position: absolute; left: 62px; top: 387px; width: 1074px; height: 332px; background: var(--paper); }
  .quote-mark { position: absolute; top: 30px; font-size: 180px; line-height: 1; font-weight: 800; color: #b5b5b5; font-family: Georgia, serif; }
  .quote p { position: absolute; left: 240px; top: 72px; width: 600px; text-align: center; font-size: 13px; line-height: 24px; }
  .quote .who { position: absolute; left: 0; width: 1074px; top: 248px; text-align: center; font-size: 15px; line-height: 24px; }
  .arrow { position: absolute; top: 255px; width: 46px; height: 46px; border-radius: 50%; display: flex; align-items: center; justify-content: center; }

  /* contact */
  .contact { top: 3951px; height: 507px; background: var(--black); color: var(--white); }
  .contact h2 { position: absolute; left: 62px; top: 78px; font-size: 56px; line-height: 88px; font-weight: 700; }
  .contact .intro { position: absolute; left: 62px; top: 270px; width: 420px; font-size: 13px; line-height: 22px; }
  .contact .mail { position: absolute; left: 62px; top: 398px; display: flex; align-items: center; gap: 14px; font-size: 14px; }
  .dot { width: 32px; height: 32px; border-radius: 50%; background: var(--grad); display: flex; align-items: center; justify-content: center; }
  .field { position: absolute; left: 610px; width: 526px; height: 42px; background: var(--white); color: #888; font-size: 12px; display: flex; align-items: center; gap: 16px; padding-left: 20px; }
  .field.area { height: 98px; align-items: flex-start; padding-top: 18px; }
  .submit { left: 610px; top: 440px; width: 526px; height: 46px; font-size: 15px; }

  /* footer */
  .site-footer { top: 4458px; height: 122px; background: var(--white); }
  .site-footer .wordmark { position: absolute; left: 62px; top: 38px; }
  .site-footer .legal { position: absolute; left: 397px; top: 52px; font-size: 15px; }
  .subscribe { position: absolute; left: 830px; top: 42px; display: flex; }
  .subscribe span { width: 192px; height: 34px; background: var(--paper); color: #888; font-size: 12px; display: flex; align-items: center; padding-left: 12px; }
  .subscribe b { width: 114px; height: 34px; background: var(--grad); color: var(--white); font-size: 13px; font-weight: 600; display: flex; align-items: center; justify-content: center; }
</style>
</head>
<body>

<header class="site-header">
  <div class="abs wordmark">VERDI</div>
  <nav class="nav"><span>Home</span><span>Membership</span><span>Organizations</span><span class="contact">Contact</span></nav>
</header>

<section class="hero">
  <div class="hero-art" role="img" aria-label="Close-up photograph of a white and pink blossom against dark leaves"></div>
  <h1>Health for<br>everyone</h1>
  <p>All-Inclusive Holistic Wellness&nbsp; $25 / month Time tested science changing the lives of millions at a price everyone can afford.</p>
  <div class="play"><svg width="18" height="18" viewBox="0 0 18 18"><path d="M5 3 L15 9 L5 15 Z" fill="#000"/></svg></div>
</section>

<section class="features">
  <div class="feature" style="left:62px;top:66px"><svg width="44" height="44" viewBox="0 0 44 44"><circle cx="22" cy="20" r="16" fill="var(--orange)"/><path d="M14 34 L10 42 L22 35 Z" fill="var(--orange)"/><rect x="14" y="14" width="16" height="3" fill="#fff"/><rect x="14" y="21" width="12" height="3" fill="#fff"/></svg><span>1 on 1 with Holistic<br>Doctors &amp; Unlimited<br>Texting</span></div>
  <div class="feature" style="left:426px;top:66px"><svg width="44" height="44" viewBox="0 0 44 44"><rect x="12" y="4" width="20" height="8" fill="var(--orange)"/><rect x="8" y="12" width="28" height="30" rx="4" fill="var(--yellow)"/><circle cx="22" cy="27" r="7" fill="var(--orange)"/></svg><span>Personalized Custom<br>Supplements</span></div>
  <div class="feature" style="left:790px;top:66px"><svg width="44" height="44" viewBox="0 0 44 44"><rect x="16" y="4" width="8" height="28" fill="var(--orange)"/><rect x="6" y="34" width="30" height="6" fill="var(--yellow)"/><rect x="26" y="16" width="10" height="14" fill="var(--yellow)"/></svg><span>Gut, Hormone &amp;<br>Cellular Lab Tests</span></div>
  <div class="feature" style="left:62px;top:215px"><svg width="44" height="44" viewBox="0 0 44 44"><rect x="14" y="6" width="28" height="20" fill="var(--yellow)"/><circle cx="10" cy="14" r="6" fill="var(--orange)"/><rect x="4" y="22" width="12" height="20" fill="var(--orange)"/></svg><span>Unlimited Classes</span></div>
  <div class="feature" style="left:426px;top:215px"><svg width="44" height="44" viewBox="0 0 44 44"><circle cx="22" cy="12" r="6" fill="var(--orange)"/><path d="M8 38 Q22 16 36 38 Z" fill="var(--yellow)"/><rect x="4" y="38" width="36" height="4" fill="var(--orange)"/></svg><span>Free Yoga, Meditation &amp;<br>Health Essentials By<br>Star Practitioners</span></div>
  <div class="feature" style="left:790px;top:215px"><svg width="44" height="44" viewBox="0 0 44 44"><rect x="4" y="8" width="22" height="16" fill="var(--yellow)"/><circle cx="34" cy="14" r="6" fill="var(--orange)"/><rect x="28" y="22" width="12" height="20" fill="var(--orange)"/><rect x="6" y="28" width="18" height="4" fill="var(--orange)"/></svg><span>Workshops</span></div>
</section>

<section class="how">
  <h2><span class="accent">How It</span> Works</h2>
  <div class="copy">
    <p>Sign-up and get a full read of your unique constitution and what makes it thrive with a custom plan made one on one with your on-demand holistic Doctor/Educator.</p>
    <p>Unlimited texting to address your plan or any other concern you have about your health.</p>
  </div>
  <div class="btn" style="left:62px;top:315px;width:154px;height:46px">View Plan</div>

  <div class="step-num" style="top:78px">01</div>
  <div class="step" style="top:77px"><svg width="36" height="36" viewBox="0 0 36 36"><rect x="14" y="4" width="18" height="28" fill="var(--yellow)"/><path d="M2 18 H20 M14 12 L20 18 L14 24" stroke="var(--orange)" stroke-width="4" fill="none"/></svg>Sign Up</div>
  <div class="step-num" style="top:184px">02</div>
  <div class="step" style="top:184px"><svg width="36" height="36" viewBox="0 0 36 36"><rect x="6" y="4" width="24" height="28" fill="var(--yellow)"/><rect x="10" y="10" width="16" height="3" fill="var(--orange)"/><rect x="10" y="17" width="16" height="3" fill="var(--orange)"/><rect x="10" y="24" width="10" height="3" fill="var(--orange)"/></svg>Get a full read of your<br>constitution</div>
  <div class="step-num" style="top:290px">03</div>
  <div class="step" style="top:291px"><svg width="36" height="36" viewBox="0 0 36 36"><path d="M4 22 L22 4 H32 V14 L14 32 Z" fill="var(--orange)"/><circle cx="26" cy="10" r="3" fill="#fff"/></svg>Get a customer plan</div>
</section>

<section class="pattern pattern-dark" role="img" aria-label="Decorative band of repeating dark arch shapes"></section>

<section class="trust">
  <h2>Our Clients Trust Us to Provide <span class="accent-y">Holistic</span> <span class="accent">Health for Their Team</span>, So Should You!</h2>
  <div class="pillar" style="left:62px"><svg width="68" height="68" viewBox="0 0 68 68"><rect x="6" y="6" width="26" height="26" fill="var(--orange)"/><rect x="34" y="34" width="28" height="28" fill="var(--yellow)"/><rect x="6" y="34" width="26" height="28" fill="var(--orange)"/><circle cx="44" cy="22" r="8" fill="var(--yellow)"/></svg>Any Challenge</div>
  <div class="pillar" style="left:426px"><svg width="68" height="68" viewBox="0 0 68 68"><circle cx="34" cy="34" r="30" fill="var(--orange)"/><circle cx="34" cy="34" r="22" fill="var(--yellow)"/><path d="M34 18 V34 L44 42" stroke="var(--orange)" stroke-width="4" fill="none"/></svg>Anytime</div>
  <div class="pillar" style="left:790px"><svg width="68" height="68" viewBox="0 0 68 68"><path d="M34 4 A16 16 0 0 1 50 20 C50 32 34 48 34 48 C34 48 18 32 18 20 A16 16 0 0 1 34 4 Z" fill="var(--orange)"/><circle cx="34" cy="20" r="6" fill="#fff"/><path d="M6 62 L18 46 H50 L62 62 Z" fill="var(--yellow)"/></svg>Anywhere</div>
  <div class="trusted"><span class="accent">Trusted by :-</span>&nbsp; Northfield Outfitters</div>
</section>

<section class="enterprise">
  <h2><span class="accent">Verdi</span> for<br>Enterprise</h2>
  <p class="lead">We're all feeling a strain on our health these days</p>
  <div class="body">
    <p>Leaders of industry aren't accidental, they know employee retention &amp; experience work in their favor.</p>
    <p>In these tumultuous times, Solace brings much-needed relief and benefits to teams that bring their all in return.</p>
  </div>
  <div class="btn" style="left:60px;top:427px;width:192px;height:44px">Verdi for Enterprise</div>
  <div class="spa-art" role="img" aria-label="Spa arrangement of flowers, candles, bath salts and rolled towels"></div>
</section>

<section class="care">
  <h2><span class="accent">Human Care</span><br>Powered by Technology</h2>
  <div class="copy">All Your Mind Body Needs Met In One Place<br>All practitioners work collaboratively to provide the best care.</div>
  <div class="btn" style="left:62px;top:282px;width:124px;height:46px">View More</div>
  <div class="rings" role="img" aria-label="Concentric yellow and orange ring graphic"></div>
</section>

<section class="pattern pattern-light" role="img" aria-label="Decorative band of repeating light grey arch shapes"></section>

<section class="stats">
  <div class="stat-box stat-left">
    <div class="claim"><span class="accent">Clinically proven to help people</span> not only feel better, but thrive.</div>
    <div class="big" style="left:305px;top:68px">80%</div>
    <div class="abs" style="left:312px;top:185px;font-size:26px;font-weight:800;color:var(--orange)">VERDI</div>
    <div class="big" style="left:493px;top:68px">20%</div>
    <div class="abs" style="left:497px;top:190px;font-size:15px;line-height:22px">Leading corporate<br>health programs</div>
  </div>
  <div class="stat-box stat-right">
    <h3><span class="accent">Members love</span> the easy &amp; effective experience.</h3>
    <div class="big" style="left:28px;top:135px;font-size:100px">5</div>
    <svg class="abs" style="left:98px;top:185px" width="46" height="44" viewBox="0 0 24 23"><path d="M12 0 L15 8 H24 L17 13 L20 22 L12 17 L4 22 L7 13 L0 8 H9 Z" fill="var(--yellow)"/></svg>
    <div class="abs" style="left:186px;top:182px;font-size:15px;line-height:22px">average rating after<br>every care session.</div>
  </div>
  <div class="quote">
    <div class="quote-mark" style="left:40px">“</div>
    <div class="quote-mark" style="left:930px">”</div>
    <p>Anytime I'm feeling tired or stressed I just get up and pass by the classes by Solace and I'm instantly perked up and happy again!&nbsp; Solace has been an excellent enhancement at Northfield Outfitters and well needed for everyone.&nbsp; Employees rave about it and frequently ask for more to be added and are getting along better.&nbsp; Ultimately they are more excited about coming to work, automatically enhancing their performance.</p>
    <div class="who"><b>MARIN</b><br>Human Resources | Northfield Outfitters</div>
    <div class="arrow" style="left:62px;border:1.5px solid #000"><svg width="14" height="14" viewBox="0 0 14 14"><path d="M9 2 L4 7 L9 12" stroke="#000" stroke-width="1.6" fill="none"/></svg></div>
    <div class="arrow" style="left:966px;background:#000"><svg width="14" height="14" viewBox="0 0 14 14"><path d="M5 2 L10 7 L5 12" stroke="#fff" stroke-width="1.6" fill="none"/></svg></div>
  </div>
</section>

<section class="contact">
  <h2>We'd <span class="accent-y">Love To</span><br><span class="accent">Hear</span> From You</h2>
  <p class="intro">Tell us a little about you and your company to see if you qualify for our membership-based model at no cost to your company.</p>
  <div class="mail"><span class="dot"><svg width="14" height="10" viewBox="0 0 14 10"><rect width="14" height="10" fill="#fff"/><path d="M0 0 L7 6 L14 0" stroke="var(--orange)" fill="none"/></svg></span>info@verdihealth.example</div>

  <div class="field" style="top:59px"><svg width="12" height="12" viewBox="0 0 12 12"><circle cx="6" cy="3.5" r="3" fill="var(--orange)"/><path d="M0 12 Q6 4 12 12 Z" fill="var(--yellow)"/></svg>Name</div>
  <div class="field" style="top:114px"><svg width="12" height="10" viewBox="0 0 12 10"><rect width="12" height="10" fill="var(--orange)"/><path d="M0 0 L6 5 L12 0" stroke="#fff" fill="none"/></svg>e-Mail</div>
  <div class="field" style="top:170px"><svg width="10" height="13" viewBox="0 0 10 13"><path d="M5 0 A5 5 0 0 1 10 5 C10 8 5 13 5 13 C5 13 0 8 0 5 A5 5 0 0 1 5 0 Z" fill="var(--orange)"/></svg>How many people in your location?</div>
  <div class="field" style="top:226px"><svg width="12" height="12" viewBox="0 0 12 12"><circle cx="6" cy="3.5" r="3" fill="var(--orange)"/><path d="M0 12 Q6 4 12 12 Z" fill="var(--yellow)"/></svg>How many locations?</div>
  <div class="field area" style="top:282px"><svg width="12" height="12" viewBox="0 0 12 12"><rect width="12" height="9" fill="var(--orange)"/><path d="M2 9 L2 12 L6 9 Z" fill="var(--orange)"/></svg>Anything else we can help with you?</div>
  <div class="btn submit">Submit</div>
</section>

<footer class="site-footer">
  <div class="wordmark">VERDI</div>
  <div class="legal">© 2025 Verdi | All rights reserved.</div>
  <div class="subscribe"><span>Enter your e-mail here</span><b>Subscribe</b></div>
</footer>

</body>
</html>
```